Kestrel Signs Facebook Banner Design

Design a facebook banner for a sign company. I would like to have a modern approach to it.

Product Offering:
Signs
Banners
Decals
Commercial Wraps

```html
<!DOCTYPE html>
<html lang="en">
<head>
<meta charset="utf-8">
<title>Kestrel Signs – Facebook Banner</title>
<link rel="stylesheet" href="https://fonts.googleapis.com/css2?family=Orbitron:wght@800&family=Ubuntu:wght@500;700&display=swap">
<style>
  :root {
    --backdrop: #b3b3b3;
    --paper: #ffffff;
    --charcoal: #353535;
    --slate: #4d4d4f;
    --signal-red: #e8343a;
    --ink-light: #ffffff;
  }
  html, body {
    margin: 0;
    padding: 0;
    width: 1200px;
    height: 594px;
    overflow: hidden;
    background: var(--backdrop);
  }
  .banner-canvas {
    display: block;
    width: 1200px;
    height: 594px;
  }
  .panel-paper { fill: var(--paper); }
  .panel-dark { fill: var(--charcoal); }
  .accent-fill { fill: url(#accent-tone); }
  .gradient-slate { stop-color: var(--slate); }
  .gradient-red { stop-color: var(--signal-red); }
  .brand-name {
    font-family: "Ubuntu", sans-serif;
    font-weight: 700;
    fill: var(--signal-red);
    letter-spacing: 2px;
  }
  .offer-heading {
    font-family: "Orbitron", sans-serif;
    font-weight: 800;
    font-size: 40px;
    fill: var(--ink-light);
  }
  .offer-item {
    font-family: "Ubuntu", sans-serif;
    font-weight: 500;
    font-size: 34px;
    fill: var(--ink-light);
  }
  .tick-badge { fill: var(--signal-red); }
  .tick-mark {
    fill: none;
    stroke: var(--ink-light);
    stroke-width: 3.2;
    stroke-linecap: round;
    stroke-linejoin: round;
  }
</style>
</head>
<body>
<svg class="banner-canvas" viewBox="0 0 1391 689" xmlns="http://www.w3.org/2000/svg" aria-labelledby="banner-title">
  <title id="banner-title">Kestrel Signs – Product Offering: Signs, Banners, Decals, Commercial Wraps</title>
  <defs>
    <clipPath id="banner-area">
      <rect x="96" y="95" width="1200" height="499"/>
    </clipPath>
    <linearGradient id="accent-tone" x1="0" y1="0" x2="0" y2="1">
      <stop class="gradient-slate" offset="0"/>
      <stop class="gradient-red" offset="1"/>
    </linearGradient>
  </defs>

  <g class="banner" clip-path="url(#banner-area)">
    <rect class="panel-paper" x="96" y="95" width="1200" height="499"/>
    <polygon class="panel-dark" points="657,95 1296,95 1296,594 900,594"/>

    <g class="accent-area" role="img" aria-label="Angled red and grey stripe decoration">
      <polygon class="accent-fill" points="520,95 657,95 943,594 697,594"/>
    </g>
    <g class="accent-area" role="img" aria-label="Angled red and grey stripe decoration">
      <polygon class="accent-fill" points="96,290 130,281 313,594 96,594"/>
    </g>

    <text class="brand-name" x="367" y="293" font-size="58" text-anchor="middle">KESTREL</text>
    <text class="brand-name" x="372" y="340" font-size="50" text-anchor="middle">SIGNS</text>

    <text class="offer-heading" x="760" y="214" textLength="503" lengthAdjust="spacingAndGlyphs">PRODUCT OFFERING</text>

    <g class="offer-list">
      <g class="offer-row">
        <circle class="tick-badge" cx="982" cy="292" r="17"/>
        <polyline class="tick-mark" points="975,292 980,297 989,287"/>
        <text class="offer-item" x="1017" y="305">Signs</text>
      </g>
      <g class="offer-row">
        <circle class="tick-badge" cx="982" cy="348" r="17"/>
        <polyline class="tick-mark" points="975,348 980,353 989,343"/>
        <text class="offer-item" x="1017" y="361">Banners</text>
      </g>
      <g class="offer-row">
        <circle class="tick-badge" cx="982" cy="405" r="17"/>
        <polyline class="tick-mark" points="975,405 980,410 989,400"/>
        <text class="offer-item" x="1017" y="418">Decals</text>
      </g>
      <g class="offer-row">
        <circle class="tick-badge" cx="982" cy="461" r="17"/>
        <polyline class="tick-mark" points="975,461 980,466 989,456"/>
        <text class="offer-item" x="1017" y="474">Commercial</text>
        <text class="offer-item" x="1017" y="516">Wraps</text>
      </g>
    </g>
  </g>
</svg>
</body>
</html>
```